Advertisement Design Project

I would like to have some advertisement ideas to promote my business. Our company provides credit repair, tax preparation, notary service, ledger preparation (for small businesses and independent contractors) tax restoration (help people with liens, levy, garnishments, etc. by negotiating with the DQV in these matters)

The name of our company is Tamberly Financing
Our "Jubilatrix" program focuses on tax preparation, restoration, and credit repair.
Our "Maple Step" program prepares ledgers for small business and independent contractors by preparing monthly ledgers so that at tax season they are not having to look everywhere for their receipts in order to get all deductions due to them during the tax season.

We need something that is catchy and will gain attention

attached is our logo. Our slogan is "Happiness, Restored!"

Thank you!

Target Market(s)

The financially distressed
Small business owners
Independent contractors
businesses that rely on credit worthy clients to do business with

Industry/Entity Type

Small Business

Requirements
Must have
• great pictures
nice layout

```html
<!DOCTYPE html>
<html lang="en">
<head>
<meta charset="utf-8">
<title>Jubilatrix Program – Tamberly Financing</title>
<link rel="stylesheet" href="https://fonts.googleapis.com/css2?family=Arimo:wght@400;700&family=Cinzel:wght@400;600&family=Open+Sans:wght@400&family=Roboto+Condensed:wght@400;700&family=Source+Sans+3:wght@400&display=swap">
<style>
  :root {
    --navy: #133e66;
    --navy-deep: #0f3459;
    --sky: #4f8fc8;
    --orange: #f4a21c;
    --ink: #2b2b2b;
    --text: #1d1d1d;
    --black: #0a0a0a;
    --white: #ffffff;
    --silver: #e6e8ea;
    --frame: #9fb2c4;
  }
  * { box-sizing: border-box; margin: 0; padding: 0; }
  html, body { width: 953px; height: 1200px; overflow: hidden; background: var(--white); }
  .flyer { position: relative; width: 953px; height: 1200px; overflow: hidden; background: var(--white); font-family: "Open Sans", sans-serif; }
  .shape-layer { position: absolute; left: 0; top: 0; width: 953px; height: 1200px; }
  .headline { position: absolute; left: 65px; font-family: "Arimo", sans-serif; font-weight: 700; white-space: nowrap; }
  .headline--offer { top: 50px; font-size: 54px; color: var(--orange); letter-spacing: 2px; }
  .headline--program { top: 108px; font-size: 62px; color: var(--silver); text-shadow: 2px 3px 4px rgba(0,0,0,.45); }
  .intro { position: absolute; left: 65px; top: 312px; width: 446px; font-size: 12.6px; line-height: 18px; color: var(--text); text-align: justify; z-index: 2; }
  .photo { position: absolute; }
  .photo--coins-stack { left: 99px; top: 440px; width: 277px; height: 195px; background: radial-gradient(ellipse at center, #eceef0 0%, #f7f8f9 60%, rgba(255,255,255,0) 100%); }
  .photo--hand-tree { left: 75px; top: 725px; width: 378px; height: 307px; background: linear-gradient(180deg, #5f7f3a 0%, #8aa052 45%, #d9b59a 80%, #f3e3d6 100%); border-radius: 40% 40% 20% 20%; }
  .photo--coins-side { left: 445px; top: 912px; width: 169px; height: 135px; background: linear-gradient(180deg, #f2f3f4 0%, #dfe2e5 100%); border-radius: 30px; }
  .program-name { position: absolute; left: 60px; top: 628px; font-family: "Source Sans 3", sans-serif; font-size: 66px; color: var(--navy); line-height: 1; }
  .brand-box { position: absolute; left: 619px; top: 277px; width: 270px; height: 260px; border: 3px solid var(--frame); padding: 6px; background: var(--white); }
  .brand-box__inner { width: 100%; height: 100%; background: var(--navy); display: flex; align-items: flex-end; justify-content: center; padding-bottom: 30px; }
  .brand-box__name { font-family: "Cinzel", serif; font-size: 19px; color: var(--white); }
  .slogan { position: absolute; left: 610px; top: 558px; width: 290px; text-align: center; font-family: "Cinzel", serif; font-weight: 600; font-size: 38px; line-height: 42px; color: var(--ink); letter-spacing: 1px; }
  .services-title { position: absolute; left: 594px; top: 706px; width: 359px; height: 53px; background: var(--navy); border-radius: 27px 0 0 27px; color: var(--white); font-family: "Roboto Condensed", sans-serif; font-size: 33px; letter-spacing: 3px; line-height: 53px; padding-left: 44px; }
  .services { position: absolute; right: 64px; top: 790px; list-style: none; text-align: right; }
  .services__item { display: flex; align-items: center; justify-content: flex-end; gap: 8px; height: 44.3px; font-family: "Roboto Condensed", sans-serif; font-weight: 700; font-size: 25px; color: var(--text); }
  .services__tick { width: 30px; height: 30px; flex: none; }
  .footer-note { position: absolute; left: 528px; top: 1102px; font-size: 12.5px; color: var(--white); white-space: nowrap; }
  .call { position: absolute; left: 63px; top: 1142px; color: var(--white); font-family: "Arimo", sans-serif; white-space: nowrap; }
  .call__label { font-size: 19px; letter-spacing: 2px; }
  .call__number { font-size: 27px; font-weight: 700; }
  .website { position: absolute; left: 419px; top: 1140px; color: var(--white); font-family: "Arimo", sans-serif; font-weight: 700; font-size: 29px; letter-spacing: 2.5px; white-space: nowrap; }
</style>
</head>
<body>
<main class="flyer">
  <svg class="shape-layer" viewBox="0 0 953 1200" aria-hidden="true">
    <path d="M0 0H953V200C800 210 640 252 460 262C300 270 140 230 0 210Z" fill="var(--navy)"/>
    <path d="M0 212C140 232 300 270 470 262C300 290 140 300 0 300Z" fill="var(--white)"/>
    <path d="M0 210C130 230 260 262 420 264C280 276 120 265 0 262Z" fill="var(--orange)"/>
    <path d="M953 200V280C820 260 700 262 470 264C660 252 800 212 953 200Z" fill="var(--sky)"/>
    <path d="M0 1075C250 1060 520 1095 953 1040V1200H0Z" fill="var(--black)"/>
    <path d="M0 1040C160 1090 350 1090 520 1080C350 1095 180 1095 0 1075Z" fill="#3a4aa6"/>
    <path d="M520 1080C700 1070 850 1040 953 1010V1040C830 1065 700 1078 520 1080Z" fill="var(--orange)"/>
    <path d="M594 700H953V706H620C606 706 598 702 594 700Z" fill="var(--sky)"/>
  </svg>

  <h1 class="headline headline--offer">We Offering</h1>
  <h2 class="headline headline--program">Jubilatrix Program</h2>

  <div class="photo photo--coins-stack" role="img" aria-label="Stack of silver coins fading into the background"></div>

  <p class="intro">Our Jubilatrix program enables our clients to find solutions for financial situations that are keeping them from achieving their goal of ownership and living a fulfilled life. Our Jubilatrix program will help you settle your debt to the DQV, alleviate your credit burden with your creditors, and assist with some light bookkeeping that will make things easier during the tax season for small businesses and independent contractors. There is no reason to live a stressfull life when a solution is being offered to you. Our fees are reasonable and our service is fantastic. Our goal is to build a cliente base that will be happy with our service, and appreciate our company culture and at the same time become customers for life.</p>

  <div class="program-name">Jubilatrix</div>

  <div class="photo photo--hand-tree" role="img" aria-label="Open hand holding gold coins with a small green tree growing from them"></div>
  <div class="photo photo--coins-side" role="img" aria-label="Stacks of silver coins"></div>

  <div class="brand-box">
    <div class="brand-box__inner"><span class="brand-box__name">Tamberly Financing</span></div>
  </div>

  <p class="slogan">HAPPINESS,<br>RESTORED!</p>

  <div class="services-title">WE PROVIDE</div>
  <ul class="services">
    <li class="services__item"><svg class="services__tick" viewBox="0 0 30 30"><circle cx="14" cy="16" r="11" fill="none" stroke="var(--orange)" stroke-width="2.5"/><path d="M8 15L13 21L27 4" fill="none" stroke="var(--navy)" stroke-width="3.5" stroke-linecap="round"/></svg>TAX PREPARATION</li>
    <li class="services__item"><svg class="services__tick" viewBox="0 0 30 30"><circle cx="14" cy="16" r="11" fill="none" stroke="var(--orange)" stroke-width="2.5"/><path d="M8 15L13 21L27 4" fill="none" stroke="var(--navy)" stroke-width="3.5" stroke-linecap="round"/></svg>RESTORATION</li>
    <li class="services__item"><svg class="services__tick" viewBox="0 0 30 30"><circle cx="14" cy="16" r="11" fill="none" stroke="var(--orange)" stroke-width="2.5"/><path d="M8 15L13 21L27 4" fill="none" stroke="var(--navy)" stroke-width="3.5" stroke-linecap="round"/></svg>CREDIT REPAIR</li>
    <li class="services__item"><svg class="services__tick" viewBox="0 0 30 30"><circle cx="14" cy="16" r="11" fill="none" stroke="var(--orange)" stroke-width="2.5"/><path d="M8 15L13 21L27 4" fill="none" stroke="var(--navy)" stroke-width="3.5" stroke-linecap="round"/></svg>LEDGER PREPARATION</li>
    <li class="services__item"><svg class="services__tick" viewBox="0 0 30 30"><circle cx="14" cy="16" r="11" fill="none" stroke="var(--orange)" stroke-width="2.5"/><path d="M8 15L13 21L27 4" fill="none" stroke="var(--navy)" stroke-width="3.5" stroke-linecap="round"/></svg>TAX RESTORATION</li>
  </ul>

  <p class="footer-note">Please feel free to browse our website for tools helpful to your needs</p>
  <p class="call"><span class="call__label">CALL US: </span><span class="call__number">012.555.0147</span></p>
  <p class="website">www.tamberlyfinancing.com</p>
</main>
</body>
</html>
```